Business Card for Field Lotus-Eco Friendly Organic Clothing Brand

We are looking for an amazing business card for our eco friendly, organic clothing brand. We are thinking maybe a business card with a peel off sticker on the back, since our hanging clothing tag is a peel off sticker on the back. I will attach our hang tag so we can make sure we stay in line with our design. I've also attached a bag we are doing because I do like the scattered emblem look as well.

```html
<!DOCTYPE html>
<html lang="en">
<head>
<meta charset="utf-8">
<title>Field Lotus – Business Card</title>
<link href="https://fonts.googleapis.com/css2?family=Arimo:wght@400;700&display=swap" rel="stylesheet">
<style>
  :root{
    --stage:#e9e6e1;
    --paper:#ffffff;
    --paper-shade:#f1f1f1;
    --ink:#1d1d1d;
    --ink-soft:#6d6d6d;
    --gold:#d9a21b;
    --gold-light:#f2d27a;
    --night:#0c0c0c;
    --night-soft:#222222;
  }
  *{box-sizing:border-box;margin:0;padding:0}
  html,body{width:1200px;height:950px;overflow:hidden}
  body{background:var(--stage);font-family:"Arimo",Arial,sans-serif;color:var(--ink)}
  .canvas{position:relative;width:1200px;height:950px}
  .card{position:absolute;left:220px;width:760px;height:434px;border-radius:6px;overflow:hidden;box-shadow:0 10px 28px rgba(0,0,0,.22)}
  .card--front{top:26px;background:linear-gradient(180deg,var(--paper) 55%,var(--paper-shade))}
  .card--back{top:490px;background:var(--night)}

  /* front */
  .holder{position:absolute;left:52px;top:118px}
  .holder__name{font-size:30px;font-weight:700;letter-spacing:.3px}
  .holder__role{font-size:19px;margin-top:4px}
  .rule{position:absolute;left:52px;right:40px;top:190px;height:2px;background:var(--ink)}
  .contacts{position:absolute;left:52px;top:208px;list-style:none}
  .contacts li{display:flex;align-items:center;gap:12px;font-size:20px;line-height:31px}
  .contacts svg{width:20px;height:20px;fill:var(--gold);flex:none}
  .address{position:absolute;right:46px;bottom:46px;text-align:right;font-size:21px;line-height:30px;color:var(--ink-soft)}
  .brand{position:absolute;right:46px;top:66px;display:flex;align-items:center;gap:12px}
  .brand__square{width:34px;height:34px;background:var(--gold)}
  .brand__name{font-size:30px;font-weight:700;color:var(--ink)}

  /* back */
  .back-pattern{position:absolute;inset:0;background:radial-gradient(ellipse at 50% 40%,var(--night-soft),var(--night) 75%)}
  .sticker{position:absolute;left:190px;top:120px;width:380px;height:150px;border:5px solid var(--gold);border-radius:14px;padding:10px;background:var(--night)}
  .sticker__art{width:100%;height:100%;border-radius:8px;background:linear-gradient(90deg,#2a2210,#5a4513 50%,#2a2210)}
  .site{position:absolute;left:0;right:0;top:300px;text-align:center;font-size:20px;letter-spacing:2px;color:#bdbdbd}
</style>
</head>
<body>
<main class="canvas">
  <section class="card card--front" aria-label="Business card front">
    <div class="brand">
      <span class="brand__square"></span>
      <span class="brand__name">Field Lotus</span>
    </div>
    <div class="holder">
      <p class="holder__name">Alan Brook</p>
      <p class="holder__role">President</p>
    </div>
    <div class="rule"></div>
    <ul class="contacts">
      <li><svg viewBox="0 0 24 24"><path d="M6.6 10.8a15 15 0 0 0 6.6 6.6l2.2-2.2c.3-.3.7-.4 1-.2 1.1.4 2.3.6 3.6.6.6 0 1 .4 1 1V20c0 .6-.4 1-1 1A17 17 0 0 1 3 4c0-.6.4-1 1-1h3.5c.6 0 1 .4 1 1 0 1.3.2 2.5.6 3.6.1.3 0 .7-.2 1z"/></svg>555 0142 7781</li>
      <li><svg viewBox="0 0 24 24"><path d="M7 1h10a2 2 0 0 1 2 2v18a2 2 0 0 1-2 2H7a2 2 0 0 1-2-2V3a2 2 0 0 1 2-2zm0 3v14h10V4zm5 15.5a1 1 0 1 0 0 2 1 1 0 0 0 0-2z"/></svg>555 0198 3046</li>
      <li><svg viewBox="0 0 24 24"><path d="M6 2h10l2 2v5H6zM3 10h18a2 2 0 0 1 2 2v7H1v-7a2 2 0 0 1 2-2zm3 8h12v4H6z"/></svg>555 0127 6459</li>
      <li><svg viewBox="0 0 24 24"><path d="M2 5h20v14H2zm2 2v.5l8 5.5 8-5.5V7z"/></svg>info@fieldlotus.com</li>
    </ul>
    <address class="address" style="font-style:normal">2190 Alder Lane<br>Maple Grove, NY 11020</address>
  </section>

  <section class="card card--back" aria-label="Business card back">
    <div class="back-pattern" role="img" aria-label="Faint scattered words and symbols of peace and calm"></div>
    <div class="sticker">
      <div class="sticker__art" role="img" aria-label="Gold sticker emblems: meditating figure, heart, peace sign and hand"></div>
    </div>
    <p class="site">www.fieldlotus.com</p>
  </section>
</main>
</body>
</html>
```